Wordpress website design for membership site

I need a wordpress website designed for a membership site specializing in member video recordings and storage. I need the site to be simplistic but fully functional. I want a minimalistic landing and member page. The member page needs to be able to showcase the members recorded videos amd utilize a GUI system of navigation utilizing graphical buttons. Member signup page needs to be fully functional to include email verification and password change/recovery functionality.

Coding

Coded - Design and coding required

Number of Pages Required

3 page

Font styles to use
Sans Serif

Colors

Designer to choose colors to be used in the design.

Requirements
Must have
• The project must incorporate the name ZELQON or ZELQON.com within the design.
Should not have
• Project should not use prepublished templates available online but should be unique in design and functionality.

```html
<!DOCTYPE html>
<html lang="en">
<head>
<meta charset="utf-8">
<title>ZELQON.com – Member Video Showcase</title>
<link rel="stylesheet" href="https://fonts.googleapis.com/css2?family=Orbitron:wght@500;700&family=Open+Sans:wght@400;600;700&family=Montserrat:wght@400;600&display=swap">
<style>
:root{
  --accent:#2cb8ea;
  --navy:#1f1d6e;
  --band:#302f94;
  --band-deep:#24237a;
  --btn:#3f8ee8;
  --btn-light:#5aa8f2;
  --ink:#222;
  --muted:#555;
  --line:#d6d6d6;
  --white:#fff;
  --page:#fff;
}
*{box-sizing:border-box;margin:0;padding:0}
html,body{width:1200px;height:4045px;overflow:hidden}
body{position:relative;background:var(--page);font-family:"Open Sans",sans-serif;color:var(--ink)}
.abs{position:absolute}
.heading{font-family:"Orbitron",sans-serif;font-weight:500;font-size:29px;text-align:center;width:1200px;left:0;letter-spacing:.5px}
.heading .hl{color:var(--accent)}
.btn{position:absolute;display:flex;align-items:center;justify-content:center;color:var(--white);font-family:"Open Sans",sans-serif;font-weight:600;font-size:18px;border-radius:4px}
.btn-primary{background:linear-gradient(var(--btn-light),var(--btn));border:1px solid rgba(255,255,255,.6)}
.btn-dark{background:var(--navy)}

/* hero */
.hero{top:0;left:0;width:1200px;height:660px;clip-path:polygon(0 0,100% 0,100% 580px,0 660px);
  background:linear-gradient(120deg,#3c4250 0%,#6f7786 40%,#a9aeb7 70%,#5e5246 100%)}
.topbar{top:0;left:690px;width:510px;height:48px;background:var(--accent);clip-path:polygon(28px 0,100% 0,100% 100%,0 100%);z-index:3;
  display:flex;align-items:center;gap:22px;padding-left:92px;color:var(--white);font-size:13px;font-weight:600}
.topbar .social{display:flex;gap:6px}
.dot{width:20px;height:20px;border:2px solid var(--white);border-radius:50%}
.wordmark{font-family:"Open Sans",sans-serif;font-weight:700;letter-spacing:1px}
.logo{top:58px;left:40px;z-index:3;color:var(--white);font-size:28px}
.nav{top:80px;left:445px;z-index:3;display:flex;gap:26px;color:var(--white);font-family:"Montserrat",sans-serif;font-weight:600;font-size:15px}
.nav .active{color:var(--accent)}
.hero-title{top:290px;left:0;width:1200px;text-align:center;z-index:3;color:var(--white);font-family:"Orbitron",sans-serif;font-weight:500;font-size:38px;line-height:44px}

/* featured */
.card{background:var(--white);box-shadow:0 2px 10px rgba(0,0,0,.14)}
.video-card{top:833px;width:332px;height:257px}
.video-card .media{position:absolute;left:16px;top:17px;width:300px;height:185px}
.play{position:absolute;left:126px;top:68px;width:50px;height:50px;border-radius:50%;background:rgba(255,255,255,.55)}
.play::after{content:"";position:absolute;left:20px;top:15px;border-left:15px solid #333;border-top:10px solid transparent;border-bottom:10px solid transparent}
.meta{position:absolute;top:216px;left:16px;right:16px;display:flex;justify-content:space-between;font-size:11.5px;color:var(--muted)}
.meta span{display:flex;align-items:center;gap:6px}
.arrow{top:935px;width:44px;height:44px;border-radius:50%;background:#eef0f4;display:flex;align-items:center;justify-content:center}

/* bands */
.band{left:0;width:1200px;background:linear-gradient(135deg,var(--band) 0%,#3b3aa8 45%,var(--band-deep) 100%)}
.how{top:1181px;height:720px;clip-path:polygon(0 87px,100% 0,100% 653px,0 100%)}
.step{top:1435px;width:290px;color:var(--white)}
.step svg{display:block;margin:0 auto 14px}
.step h3{font-size:17px;font-weight:700}
.step p{font-size:16px;line-height:20px}

/* news */
.news-card{top:2077px;width:327px;height:410px}
.news-card .media{position:absolute;left:19px;top:19px;width:289px;height:169px}
.news-card .date{position:absolute;left:19px;top:210px;display:flex;align-items:center;gap:10px;font-family:"Montserrat",sans-serif;font-size:16px}
.news-card .body{position:absolute;left:19px;right:16px;top:252px;font-family:"Montserrat",sans-serif;font-size:14.5px;line-height:18px}
.news-card .body b{font-weight:600;display:block}
.news-card .more{position:absolute;left:19px;top:365px;font-family:"Montserrat",sans-serif;font-size:14px;color:var(--muted)}

.about{top:2576px;height:593px;clip-path:polygon(0 81px,100% 0,100% 526px,0 100%)}
.about-text{top:2828px;left:80px;width:1040px;text-align:center;color:var(--white);font-size:16.5px;line-height:21px}

/* contact */
.field{border:1px solid var(--line);border-radius:2px;font-size:14px;font-weight:600;padding:12px 14px;color:var(--ink)}

/* footer */
.footer{top:3695px;height:350px;clip-path:polygon(0 67px,100% 0,100% 100%,0 100%)}
.footer-logo{top:3824px;left:0;width:1200px;text-align:center;color:var(--accent);font-size:30px}
.footer-nav{top:3900px;left:0;width:1200px;display:flex;justify-content:center;gap:30px;color:var(--white);font-family:"Montserrat",sans-serif;font-weight:600;font-size:15px}
.footer-nav .active{color:var(--accent)}
.footer-social{top:3948px;left:0;width:1200px;display:flex;justify-content:center;gap:6px}
.copyright{top:4002px;left:0;width:1200px;text-align:center;color:var(--white);font-size:11px;font-weight:600;letter-spacing:.5px}
</style>
</head>
<body>

<!-- Header & hero -->
<div class="abs hero" role="img" aria-label="Photo of a person using a tablet beside a cup of coffee"></div>
<div class="abs topbar">
  <span>Call Us&nbsp; 555.014.2290</span><span>Register</span><span>Login</span>
  <span class="social"><i class="dot"></i><i class="dot"></i><i class="dot"></i></span>
</div>
<div class="abs logo wordmark">ZELQON.COM</div>
<nav class="abs nav"><span class="active">HOME</span><span>FEATURED VIDEOS</span><span>HOW IT WORKS</span><span>NEWS</span><span>ABOUT</span><span>CONTACT</span></nav>
<h1 class="abs hero-title" style="font-weight:500">We make showcasing members' recorded<br>videos very easy</h1>
<a class="btn btn-dark" style="left:383px;top:388px;width:210px;height:49px;z-index:3">Create Account</a>
<a class="btn btn-primary" style="left:610px;top:388px;width:207px;height:49px;z-index:3">View Videos</a>

<!-- Featured videos -->
<h2 class="abs heading" style="top:750px"><span class="hl">Featured</span> Videos</h2>
<div class="abs arrow" style="left:5px"><svg width="12" height="16"><path d="M9 2 3 8l6 6" fill="none" stroke="#3f8ee8" stroke-width="3"/></svg></div>
<div class="abs arrow" style="left:1151px"><svg width="12" height="16"><path d="M3 2l6 6-6 6" fill="none" stroke="#3f8ee8" stroke-width="3"/></svg></div>

<div class="abs card video-card" style="left:75px">
  <div class="media" role="img" aria-label="Video thumbnail: hiker on a mountain at sunset" style="background:linear-gradient(#c98a4e,#6b4a3a 60%,#2b2224)"><span class="play"></span></div>
  <div class="meta"><span><svg width="16" height="16"><circle cx="8" cy="5" r="4" fill="#3f8ee8"/><path d="M1 16a7 6 0 0 1 14 0z" fill="#3f8ee8"/></svg>Uploaded by Cal Moreno</span><span><svg width="16" height="16"><rect x="1" y="3" width="14" height="12" fill="none" stroke="#3f8ee8" stroke-width="2"/><path d="M1 7h14" stroke="#3f8ee8" stroke-width="2"/></svg>Feb 10, 2019</span></div>
</div>
<div class="abs card video-card" style="left:434px">
  <div class="media" role="img" aria-label="Video thumbnail: busy city street at night" style="background:linear-gradient(135deg,#2a2a38,#7a5a3a 50%,#3a3540)"><span class="play"></span></div>
  <div class="meta"><span><svg width="16" height="16"><circle cx="8" cy="5" r="4" fill="#3f8ee8"/><path d="M1 16a7 6 0 0 1 14 0z" fill="#3f8ee8"/></svg>Uploaded by Ivy Tanaka</span><span><svg width="16" height="16"><rect x="1" y="3" width="14" height="12" fill="none" stroke="#3f8ee8" stroke-width="2"/><path d="M1 7h14" stroke="#3f8ee8" stroke-width="2"/></svg>Feb 10, 2019</span></div>
</div>
<div class="abs card video-card" style="left:793px">
  <div class="media" role="img" aria-label="Video thumbnail: city skyline at dusk" style="background:linear-gradient(#4a4a78,#c8663a 50%,#4a2e2a)"><span class="play"></span></div>
  <div class="meta"><span><svg width="16" height="16"><circle cx="8" cy="5" r="4" fill="#3f8ee8"/><path d="M1 16a7 6 0 0 1 14 0z" fill="#3f8ee8"/></svg>Uploaded by Rhea Lindqvist</span><span><svg width="16" height="16"><rect x="1" y="3" width="14" height="12" fill="none" stroke="#3f8ee8" stroke-width="2"/><path d="M1 7h14" stroke="#3f8ee8" stroke-width="2"/></svg>Feb 10, 2019</span></div>
</div>

<!-- How it works -->
<section class="abs band how" role="img" aria-label="Background photo of a video gallery screen under a blue tint"></section>
<h2 class="abs heading" style="top:1344px;color:#fff"><span class="hl">How It</span> Works</h2>
<div class="abs step" style="left:94px">
  <svg width="80" height="70" viewBox="0 0 80 70" fill="none" stroke="#2cb8ea" stroke-width="4"><path d="M32 8h34v54H32M32 22V8M32 48v14"/><path d="M10 35h34M32 24l12 11-12 11"/></svg>
  <h3>01. Register and Sign up</h3><p>Lorem ipsum dolor sit amet, con sectetur adipiscing elit, sed do eiusmod tempor incididunt ut.</p>
</div>
<div class="abs step" style="left:464px">
  <svg width="80" height="70" viewBox="0 0 80 70" fill="none" stroke="#2cb8ea" stroke-width="4"><path d="M10 10h22l6 8h26v40H10z"/><path d="M32 30l14 10-14 10z"/></svg>
  <h3>02. Record and Store Videos</h3><p>Lorem ipsum dolor sit amet, con sectetur adipiscing elit, sed do eiusmod tempor incididunt ut.</p>
</div>
<div class="abs step" style="left:833px">
  <svg width="80" height="70" viewBox="0 0 80 70" fill="none" stroke="#2cb8ea" stroke-width="4"><rect x="12" y="4" width="56" height="62" rx="3"/><path d="M12 16h56M12 54h56M24 4v12M40 4v12M56 4v12M24 54v12M40 54v12M56 54v12"/><path d="M34 26l14 9-14 9z"/></svg>
  <h3>03. Showcase Your Videos</h3><p>Lorem ipsum dolor sit amet, con sectetur adipiscing elit, sed do eiusmod tempor incididunt ut.</p>
</div>
<a class="btn btn-primary" style="left:494px;top:1686px;width:213px;height:48px">Get Started</a>

<!-- Latest news -->
<h2 class="abs heading" style="top:1990px"><span class="hl">Latest</span> News</h2>
<article class="abs card news-card" style="left:92px">
  <div class="media" role="img" aria-label="News photo: person silhouetted against a glowing yellow wall" style="background:linear-gradient(90deg,#3a2a10,#e0a420 40%,#5a4a38 70%,#2a2622)"></div>
  <div class="date"><svg width="20" height="20"><rect x="2" y="3" width="16" height="15" fill="none" stroke="#3f8ee8" stroke-width="2"/><path d="M2 8h16M7 12v4M11 11v5M15 13v3" stroke="#3f8ee8" stroke-width="2"/></svg>Jan 14, 2019</div>
  <div class="body"><b>Duis aute irure dolor in reprehen</b>Lorem ipsum dolor sit amet, cons ectetur adipiscing elit, sed do eius mod tempor incididunt.</div>
  <div class="more">Read more...</div>
</article>
<article class="abs card news-card" style="left:442px">
  <div class="media" role="img" aria-label="News photo: waterfront skyline at twilight" style="background:linear-gradient(#3a6aa8,#8ab0d8 45%,#1a2a48 75%,#2a4a6a)"></div>
  <div class="date"><svg width="20" height="20"><rect x="2" y="3" width="16" height="15" fill="none" stroke="#3f8ee8" stroke-width="2"/><path d="M2 8h16M7 12v4M11 11v5M15 13v3" stroke="#3f8ee8" stroke-width="2"/></svg>Jan 14, 2019</div>
  <div class="body"><b>Duis aute irure dolor in reprehen</b>Lorem ipsum dolor sit amet, cons ectetur adipiscing elit, sed do eius mod tempor incididunt.</div>
  <div class="more">Read more...</div>
</article>
<article class="abs card news-card" style="left:785px">
  <div class="media" role="img" aria-label="News photo: suburban houses in snow" style="background:linear-gradient(#a8c4e0,#d8dce0 45%,#8a6a50 60%,#eef0f2)"></div>
  <div class="date"><svg width="20" height="20"><rect x="2" y="3" width="16" height="15" fill="none" stroke="#3f8ee8" stroke-width="2"/><path d="M2 8h16M7 12v4M11 11v5M15 13v3" stroke="#3f8ee8" stroke-width="2"/></svg>Jan 14, 2019</div>
  <div class="body"><b>Duis aute irure dolor in reprehen</b>Lorem ipsum dolor sit amet, cons ectetur adipiscing elit, sed do eius mod tempor incididunt.</div>
  <div class="more">Read more...</div>
</article>

<!-- About -->
<section class="abs band about" role="img" aria-label="Background photo of hands holding a phone with a video gallery, under a blue tint"></section>
<h2 class="abs heading" style="top:2738px;color:#fff"><span class="hl">About</span> Zelqon.com</h2>
<p class="abs about-text">Lorem ipsum dolor sit amet, consectetur adipiscing elit, sed do eiusmod tempor incididunt ut labore et dolore magna aliqua. Ut enim ad minim veniam, quis nostrud exercitation ullamco laboris nisi ut aliquip ex ea commodo consequat. Duis aute iru re dolor in reprehenderit in voluptate velit esse cillum dolore eu fugiat nulla pariatur. Excepteur sint occaecat cupidatat non proident, sunt in culpa qui officia deserunt mollit anim id est laborum.</p>
<a class="btn btn-primary" style="left:494px;top:2950px;width:213px;height:52px">Learn More</a>

<!-- Contact -->
<h2 class="abs heading" style="top:3256px"><span class="hl">Contact</span> Us</h2>
<div class="abs field" style="left:113px;top:3344px;width:318px;height:46px">Your Name</div>
<div class="abs field" style="left:445px;top:3344px;width:313px;height:46px">Your Email</div>
<div class="abs field" style="left:771px;top:3344px;width:316px;height:46px">Your Subject</div>
<div class="abs field" style="left:113px;top:3404px;width:974px;height:132px">Message</div>
<a class="btn btn-dark" style="left:496px;top:3552px;width:208px;height:48px;border-radius:3px">Submit</a>

<!-- Footer -->
<footer class="abs band footer" role="img" aria-label="Background photo of a laptop with video thumbnails, under a blue tint"></footer>
<div class="abs footer-logo wordmark">ZELQON.COM</div>
<nav class="abs footer-nav"><span class="active">HOME</span><span>FEATURED VIDEOS</span><span>HOW IT WORKS</span><span>ABOUT</span><span>NEWS</span><span>CONTACT</span></nav>
<div class="abs footer-social"><i class="dot"></i><i class="dot"></i><i class="dot"></i></div>
<p class="abs copyright">COPYRIGHT © 2018 ZELQON.COM. ALL RIGHTS RESERVED.</p>

</body>
</html>
```